wedding officIate wedding day coordination wedding planning

We offer elopement packages featuring Fernbrook NC as a destination for ceremony
we offer wedding officiate services , premarital coaching
wedding planning for small events
wedding day coordination services

Industry/Entity Type

Wedding

Contact Information for Business Card

Silver Lantern
gentle vowsies & tender quiet gatherings
Marisol Pettigrew
Fernbrook NC

```html
<!DOCTYPE html>
<html lang="en">
<head>
<meta charset="utf-8">
<title>Silver Lantern — Business Card</title>
<link href="https://fonts.googleapis.com/css2?family=Arimo:wght@400&family=Cormorant+Garamond:ital,wght@1,600&display=swap" rel="stylesheet">
<style>
  :root {
    --page-bg: #6e5a46;
    --card-grey: #7b7b7b;
    --ink-white: #ffffff;
    --accent-yellow: #f2ee1e;
    --moon-light: #f4f4f4;
    --moon-shade: #d9d9d9;
    --ornament-tone: rgba(255, 255, 255, 0.16);
  }
  * { box-sizing: border-box; margin: 0; padding: 0; }
  html, body {
    width: 1000px; height: 1200px; overflow: hidden;
    background: var(--page-bg);
  }
  .canvas { position: relative; width: 1000px; height: 1200px; }
  .card {
    position: absolute; left: 37px; width: 926px; height: 541px;
    background: var(--card-grey);
  }
  .card--front { top: 42px; }
  .card--back { top: 617px; }
  .ornament-frame {
    position: absolute; inset: 8px;
    border: 26px solid var(--ornament-tone);
  }
  .moon {
    position: absolute; width: 304px; height: 304px; border-radius: 50%;
    background: radial-gradient(circle at 45% 40%, var(--moon-light) 0%, #ececec 55%, var(--moon-shade) 100%);
  }
  .card--front .moon { left: 111px; top: 119px; }
  .card--back .moon { left: 316px; top: 96px; }
  .divider {
    position: absolute; left: 485px; top: 141px; width: 2px; height: 262px;
    background: var(--ink-white);
  }
  .contact {
    position: absolute; left: 508px; top: 196px;
    font-family: "Arimo", Arial, sans-serif; color: var(--ink-white);
  }
  .contact__name {
    font-size: 30px; font-weight: 400; color: var(--accent-yellow); line-height: 1;
  }
  .contact__city { font-size: 17px; margin-top: 8px; }
  .contact__line {
    display: flex; align-items: center; gap: 8px;
    font-size: 22px; line-height: 1;
  }
  .contact__line--phone { margin-top: 34px; }
  .contact__line--mail { margin-top: 8px; }
  .contact__icon { width: 23px; height: 22px; flex: none; }
  .tagline {
    position: absolute; left: 0; right: 0; top: 428px;
    text-align: center;
    font-family: "Cormorant Garamond", Georgia, serif;
    font-style: italic; font-weight: 600; font-size: 34px;
    color: var(--ink-white);
  }
  .tagline__accent { color: var(--accent-yellow); }
</style>
</head>
<body>
<main class="canvas">
  <section class="card card--front">
    <div class="ornament-frame" role="img" aria-label="Decorative lace-style floral border"></div>
    <div class="moon" role="img" aria-label="Full moon illustration with two kissing birds on a flowering branch"></div>
    <div class="divider"></div>
    <div class="contact">
      <h1 class="contact__name">Marisol Pettigrew</h1>
      <p class="contact__city">Fernbrook NC</p>
      <p class="contact__line contact__line--phone">
        <svg class="contact__icon" viewBox="0 0 23 22" aria-hidden="true">
          <rect width="23" height="22" fill="#ffffff"/>
          <path d="M6 4 L9 4 L10 8 L8 9.5 C9 12 10.5 13.5 13 14.5 L14.5 12.5 L18.5 13.5 L18.5 16.5 C18.5 17.5 17.5 18 16.5 18 C10 17.5 5 12.5 4.5 6 C4.5 5 5 4 6 4 Z" fill="#7b7b7b"/>
        </svg>
        555 014 2290
      </p>
      <p class="contact__line contact__line--mail">
        <svg class="contact__icon" viewBox="0 0 23 22" aria-hidden="true">
          <rect width="23" height="22" fill="#ffffff"/>
          <rect x="3" y="5" width="17" height="12" fill="none" stroke="#7b7b7b" stroke-width="1.6"/>
          <path d="M3 5 L11.5 12 L20 5 M3 17 L9 11 M20 17 L14 11" fill="none" stroke="#7b7b7b" stroke-width="1.6"/>
        </svg>
        hello@silverlanternvows.com
      </p>
    </div>
  </section>

  <section class="card card--back">
    <div class="ornament-frame" role="img" aria-label="Decorative lace-style floral border"></div>
    <div class="moon" role="img" aria-label="Full moon illustration with two kissing birds on a flowering branch"></div>
    <p class="tagline">Silver Lantern gentle vowsies <span class="tagline__accent">&amp; tender quiet gatherings</span></p>
  </section>
</main>
</body>
</html>
```